Menu Design Project

We are a cafe in italy our name is "Bright Corvella Cafe & Food"

We need a new menu we offer cafes and snacks.

our web site is brightcorvella.com you can find there our logo.

We need something clean to print so we can offer to our clients a good menu.

Target Market(s)

cafe clients

Industry/Entity Type

Cafe

Requirements
Must have
• - Nice design
- Our logo
- Demo text so we can write our text

```html
<!DOCTYPE html>
<html lang="en">
<head>
<meta charset="utf-8">
<title>Bright Corvella Cafe &amp; Food — Menu</title>
<link rel="stylesheet" href="https://fonts.googleapis.com/css2?family=Oswald:wght@600;700&family=Nunito+Sans:wght@400&display=swap">
<style>
  :root {
    --ink: #141414;
    --orange: #f08a1f;
    --text: #f2f2f2;
    --muted: #8a8a8a;
    --photo-frame: #0a0a0a;
  }
  * { margin: 0; padding: 0; box-sizing: border-box; }
  html, body { width: 848px; height: 1200px; overflow: hidden; background: var(--ink); }
  .menu {
    position: relative;
    width: 848px;
    height: 1200px;
    background: var(--ink);
    font-family: "Nunito Sans", "Helvetica Neue", Arial, sans-serif;
    color: var(--text);
  }
  .top-band { position: absolute; top: 0; left: 0; width: 100%; height: 11px; background: var(--orange); }
  .menu-title {
    position: absolute; top: 52px; left: 0; width: 100%;
    text-align: center;
    font-family: "Oswald", Georgia, serif;
    font-weight: 700;
    font-size: 74px;
    line-height: 1;
    letter-spacing: 14px;
    color: #ffffff;
  }
  .section { position: absolute; }
  .section-title {
    font-family: "Oswald", Georgia, serif;
    font-weight: 600;
    font-size: 20px;
    letter-spacing: 1.5px;
    color: var(--orange);
    line-height: 1;
    margin-bottom: 30px;
  }
  .section-items { list-style: none; }
  .section-items li {
    font-size: 21px;
    line-height: 25.6px;
    letter-spacing: 2px;
  }
  .starters { left: 66px; top: 156px; }
  .soups { left: 66px; top: 365px; }
  .coffee { left: 66px; top: 545px; }
  .sandwiches { left: 430px; top: 643px; }

  .photo {
    position: absolute;
    border: 6px solid var(--photo-frame);
  }
  .photo-shake {
    left: 396px; top: 160px; width: 396px; height: 396px;
    background: radial-gradient(ellipse at 45% 45%, #e9b3a6 0%, #c98e82 30%, #b5ada3 55%, #3a2f2a 100%);
  }
  .photo-burger {
    left: 68px; top: 755px; width: 328px; height: 325px;
    background: radial-gradient(ellipse at 55% 50%, #9b5a2c 0%, #6a3a1c 40%, #c9b79a 75%, #7d6a55 100%);
  }

  .brand-name {
    position: absolute; right: 60px; top: 1020px;
    font-family: "Nunito Sans", "Helvetica Neue", Arial, sans-serif;
    font-weight: 400;
    font-size: 22px;
    line-height: 1.2;
    color: var(--orange);
    letter-spacing: 1px;
    white-space: nowrap;
  }

  .footer {
    position: absolute; left: 67px; top: 1120px;
    font-size: 10.5px;
    color: var(--muted);
    letter-spacing: 0.2px;
    white-space: nowrap;
  }
  .footer .phone { color: var(--orange); }
</style>
</head>
<body>
<main class="menu">
  <div class="top-band"></div>
  <h1 class="menu-title">MENU</h1>

  <section class="section starters">
    <h2 class="section-title">Starters</h2>
    <ul class="section-items">
      <li>Chicken strips</li>
      <li>beef and cheese sticks</li>
      <li>vegetable rolls</li>
      <li>Cheese sticks</li>
      <li>Prawn cocktail</li>
    </ul>
  </section>

  <section class="section soups">
    <h2 class="section-title">Soups</h2>
    <ul class="section-items">
      <li>Chicken soup</li>
      <li>Tomatoe soup</li>
      <li>Cucumber soup</li>
      <li>Sweet and sour</li>
    </ul>
  </section>

  <section class="section coffee">
    <h2 class="section-title">Coffee</h2>
    <ul class="section-items">
      <li>Latte</li>
      <li>Affogato</li>
      <li>Con Panna</li>
      <li>Cappachino</li>
      <li>Americano</li>
    </ul>
  </section>

  <div class="photo photo-shake" role="img" aria-label="Photo of a strawberry milkshake in a tall glass with a strawberry on the rim"></div>
  <div class="photo photo-burger" role="img" aria-label="Photo of a beef burger with fries on a plate"></div>

  <section class="section sandwiches">
    <h2 class="section-title">Sandwitches</h2>
    <ul class="section-items">
      <li>Buffalo wrap</li>
      <li>Beef salad sandwitch</li>
      <li>club sandwitch</li>
      <li>Chicken burger</li>
      <li>Beef classic burger</li>
      <li>Vegggie delight</li>
      <li>Another burger</li>
      <li>Spicy burger</li>
      <li>Hunter beef sandwitch</li>
    </ul>
  </section>

  <p class="brand-name">Bright Corvella Cafe &amp; Food</p>

  <p class="footer">Via L. Rovesta, 12. &nbsp; <span class="phone">Phone: +39 02 5550 1842 &amp; +39 333 555 0917</span> &nbsp; Email: info@brightcorvella.com</p>
</main>
</body>
</html>
```